Brookmere Osteopathy flyer

I want a clean clear DL flyer (but also want an A4 poster) promoting a new Osteopathic business in a semi rural area in Tasmania (Australia).
It can have pictures like the examples attached to show people what Osteopathy is (its like Chiropractic and physiotherapy).
I am the sole practioner and am male, so any pictures would be best to be a white male if possible.
I've attached some wording, you can use all, or none of it
I don't have a phone number for the business yet
info@brookmereosteopathy.example
www.brookmereosteopathy.example
Target Market(s)
Australians, from tradies, professionals, babies to retired people
Industry/Entity Type
Health
Look and feel

```html
<!DOCTYPE html>
<html lang="en">
<head>
<meta charset="utf-8">
<title>Brookmere Osteopathy – DL Flyer</title>
<link rel="stylesheet" href="https://fonts.googleapis.com/css2?family=Montserrat:wght@600;700;800&family=Roboto:wght@700&display=swap">
<style>
  :root{
    --orange:#f08a24;
    --orange-deep:#e0601a;
    --orange-light:#f7a640;
    --blue:#1f5e8c;
    --navy:#0f3352;
    --white:#ffffff;
    --photo-light:#c9b9a6;
    --photo-mid:#5b5550;
    --photo-dark:#1c1c1e;
  }
  *{margin:0;padding:0;box-sizing:border-box}
  html,body{width:1200px;height:2552px;overflow:hidden;background:var(--photo-dark)}
  .flyer{position:relative;width:1200px;height:2552px;overflow:hidden;font-family:"Montserrat",Arial,sans-serif;color:var(--white)}
  .hero-photo{position:absolute;inset:0;
    background:
      radial-gradient(ellipse 520px 700px at 960px 500px, rgba(236,228,218,.9), rgba(236,228,218,0) 70%),
      radial-gradient(ellipse 700px 600px at 300px 1900px, rgba(120,95,75,.55), rgba(0,0,0,0) 70%),
      linear-gradient(175deg, var(--photo-light) 0%, var(--photo-mid) 35%, var(--photo-dark) 60%, #2a2522 100%);}
  .intro-disc{position:absolute;left:-160px;top:180px;width:620px;height:620px;border-radius:50%;background:var(--blue);opacity:.85}
  .intro{position:absolute;left:112px;top:222px;width:700px}
  .intro .rule{height:22px;background:var(--orange)}
  .intro p{font-weight:700;font-size:35px;line-height:45px;padding:30px 0 32px}
  .brand-mark{position:absolute;left:548px;top:1068px;width:224px;height:224px;border-radius:50%;background:var(--navy);border:6px solid #3e86bd;display:flex;align-items:center;justify-content:center;text-align:center}
  .brand-mark span{font-weight:800;font-size:26px;line-height:32px;letter-spacing:1px;text-transform:uppercase;width:170px}
  .reasons{position:absolute;left:112px;top:1448px;width:976px}
  .reasons h2{font-family:"Roboto",Arial,sans-serif;font-weight:700;font-size:52px;line-height:56px;text-align:center;text-transform:uppercase;letter-spacing:.5px}
  .reasons ul{list-style:none;margin-top:48px}
  .reasons li{display:flex;align-items:center;font-weight:600;font-size:37px;height:64px}
  .reasons li svg{width:34px;height:34px;margin-right:32px;flex:none}
  .contact-band{position:absolute;left:0;top:2190px;width:1200px;height:362px;
    background:linear-gradient(100deg,var(--orange-deep) 0%,var(--orange) 50%,var(--orange-light) 100%)}
  .contact{position:absolute;left:0;top:2238px;width:1200px;text-align:center;font-weight:700;font-size:38px;line-height:64px}
  .contact div{display:flex;justify-content:center;align-items:center;gap:18px;margin-left:-200px}
  .contact svg{width:38px;height:38px;flex:none}
</style>
</head>
<body>
<main class="flyer">
  <div class="hero-photo" role="img" aria-label="Osteopath's hands treating the back of a patient lying face down on a treatment table"></div>
  <div class="intro-disc"></div>

  <section class="intro">
    <div class="rule"></div>
    <p>Osteopaths use a combination of joint manipulation, targeted deep tissue massage and stretching to improve function, relieve pain and support the body's ability to heal itself.</p>
    <div class="rule"></div>
  </section>

  <div class="brand-mark"><span>Brookmere Osteopathy</span></div>

  <section class="reasons">
    <h2>Common reasons<br>people visit an osteopath:</h2>
    <ul>
      <li><svg viewBox="0 0 34 34"><circle cx="17" cy="17" r="14" fill="none" stroke="#f08a24" stroke-width="4"/><circle cx="17" cy="17" r="6" fill="#f08a24"/></svg>Back / neck pain</li>
      <li><svg viewBox="0 0 34 34"><circle cx="17" cy="17" r="14" fill="none" stroke="#f08a24" stroke-width="4"/><circle cx="17" cy="17" r="6" fill="#f08a24"/></svg>Headaches / migraines</li>
      <li><svg viewBox="0 0 34 34"><circle cx="17" cy="17" r="14" fill="none" stroke="#f08a24" stroke-width="4"/><circle cx="17" cy="17" r="6" fill="#f08a24"/></svg>Joint and muscle pain</li>
      <li><svg viewBox="0 0 34 34"><circle cx="17" cy="17" r="14" fill="none" stroke="#f08a24" stroke-width="4"/><circle cx="17" cy="17" r="6" fill="#f08a24"/></svg>Pregnancy-related discomfort</li>
      <li><svg viewBox="0 0 34 34"><circle cx="17" cy="17" r="14" fill="none" stroke="#f08a24" stroke-width="4"/><circle cx="17" cy="17" r="6" fill="#f08a24"/></svg>Disc related issues</li>
      <li><svg viewBox="0 0 34 34"><circle cx="17" cy="17" r="14" fill="none" stroke="#f08a24" stroke-width="4"/><circle cx="17" cy="17" r="6" fill="#f08a24"/></svg>Sciatica</li>
      <li><svg viewBox="0 0 34 34"><circle cx="17" cy="17" r="14" fill="none" stroke="#f08a24" stroke-width="4"/><circle cx="17" cy="17" r="6" fill="#f08a24"/></svg>Plantar fasciitis</li>
      <li><svg viewBox="0 0 34 34"><circle cx="17" cy="17" r="14" fill="none" stroke="#f08a24" stroke-width="4"/><circle cx="17" cy="17" r="6" fill="#f08a24"/></svg>Tendonitis / Bursitis</li>
      <li><svg viewBox="0 0 34 34"><circle cx="17" cy="17" r="14" fill="none" stroke="#f08a24" stroke-width="4"/><circle cx="17" cy="17" r="6" fill="#f08a24"/></svg>Adhesive capsulitis (frozen shoulder)</li>
      <li><svg viewBox="0 0 34 34"><circle cx="17" cy="17" r="14" fill="none" stroke="#f08a24" stroke-width="4"/><circle cx="17" cy="17" r="6" fill="#f08a24"/></svg>Tennis / Golfers elbow</li>
    </ul>
  </section>

  <div class="contact-band"></div>
  <address class="contact" style="font-style:normal">
    <div><svg viewBox="0 0 24 24"><path fill="#fff" d="M12 2a7 7 0 0 0-7 7c0 5 7 13 7 13s7-8 7-13a7 7 0 0 0-7-7zm0 9.5A2.5 2.5 0 1 1 12 6.5a2.5 2.5 0 0 1 0 5z"/></svg>24 Wattle Creek Road, Brookmere</div>
    <div><svg viewBox="0 0 24 24"><path fill="#fff" d="M6.6 10.8a15 15 0 0 0 6.6 6.6l2.2-2.2c.3-.3.7-.4 1-.2 1.1.4 2.3.6 3.6.6.6 0 1 .4 1 1V20c0 .6-.4 1-1 1A17 17 0 0 1 3 4c0-.6.4-1 1-1h3.5c.6 0 1 .4 1 1 0 1.3.2 2.5.6 3.6.1.3 0 .7-.2 1z"/></svg>[Insert Phone Number]</div>
    <div><svg viewBox="0 0 24 24"><g fill="none" stroke="#fff" stroke-width="1.8"><circle cx="12" cy="12" r="9"/><ellipse cx="12" cy="12" rx="4" ry="9"/><path d="M3 12h18M5 7h14M5 17h14"/></g></svg>www.brookmereosteopathy.example</div>
    <div><svg viewBox="0 0 24 24"><g fill="none" stroke="#fff" stroke-width="1.8"><rect x="3" y="5" width="18" height="14" rx="1"/><path d="M3 6l9 7 9-7"/></g></svg>[info@brookmereosteopathy.example]</div>
  </address>
</main>
</body>
</html>
```